Card Design Project

A simple, funky, cool birth announcement card
Not corporate, but arty
Not childish nor girlish
No baby pictures

Text is tbc (eg name and date may change)

Front side: just the name "mira"
Should be easy to read

Back side text (in Dutch):

We vinden je nu al leuk!

20 JUNE 2013
Singapore

Dochter van Fenna Drost & Joost Kramer

Yangon, Myanmar
+95 1 73 4816
Skype: Fenna.Drost
Skype: Joost.Kramer

Size will be A6
Updates

Reason: Dear designers, At this stage we would like to have one or more designers to draft up the card (of which the final text is still tbd as the baby is yet to be born) using the typeface used on the left below (or similar!) of the newly added picture - in black - in fluorescent colours Can you get back to us in a few days? Thanks

Target Market(s)

Our funky friends in holland.

Industry/Entity Type

Baby

Requirements
Must have
• Colours, aswe are very happy to welcome this baby.
Something that makes it stand out from all other baby birth announcement cards

A6 size
Deadline 21 June
Printing will be on white (thick paper 250g)
Design for 5mm "bleedsides" all around
At least available in PDF (and other formats)
Nice to have
• We've recently moved from netherlands to Yangon
We could include the iconic thalivor pagoda

I would like for it to look like a cool party announcement

Include bright fluoriscent colours, including orange.
The enveloppe will be orange
Should not have
• Any baby stuff, soft pink dominance, childish stuff.

```html
<!DOCTYPE html>
<html lang="nl">
<head>
<meta charset="utf-8">
<title>Geboortekaart mira</title>
<link rel="stylesheet" href="https://fonts.googleapis.com/css2?family=Saira+Condensed:wght@400;500&display=swap">
<style>
  :root {
    --page: #ffffff;
    --card-deep: #0a1c9a;
    --card-mid: #1a3fd8;
    --card-light: #3f86f5;
    --card-edge: #2a47c8;
    --glow-mint: #6ff7c4;
    --ink: #ffffff;
  }
  html, body {
    margin: 0;
    padding: 0;
    width: 1200px;
    height: 1200px;
    overflow: hidden;
    background: var(--page);
  }
  .card {
    position: absolute;
    left: 42px;
    top: 42px;
    width: 1116px;
    height: 1116px;
    border-radius: 6px;
    overflow: hidden;
    border: 3px solid var(--card-edge);
    box-sizing: border-box;
    box-shadow: 0 0 14px rgba(20, 50, 200, 0.55);
    background: linear-gradient(160deg, var(--card-mid) 0%, var(--card-deep) 60%, #0b1a8a 100%);
    font-family: "Saira Condensed", "Arial Narrow", sans-serif;
    color: var(--ink);
  }
  .backdrop-art,
  .card-text {
    position: absolute;
    inset: 0;
  }
  .card-text text {
    fill: var(--ink);
    font-family: "Saira Condensed", "Arial Narrow", sans-serif;
    filter: url(#text-shadow);
  }
  .headline { font-size: 150px; font-weight: 400; }
  .date-big { font-size: 118px; font-weight: 400; }
  .date-small { font-size: 76px; font-weight: 400; }
  .parents { font-size: 68px; font-weight: 400; }
  .contact { font-size: 50px; font-weight: 400; }
  .card-text .ghost-name {
    font-size: 150px;
    font-weight: 500;
    opacity: 0.16;
    filter: none;
  }
</style>
</head>
<body>
  <div class="card">
    <svg class="backdrop-art" role="img" aria-label="Abstract backdrop of glowing mint light spots over a blue halftone wave" width="1116" height="1116" viewBox="0 0 1116 1116">
      <defs>
        <radialGradient id="mint-glow-a" cx="0.68" cy="0.28" r="0.3">
          <stop offset="0" stop-color="#6ff7c4" stop-opacity="0.55"/>
          <stop offset="1" stop-color="#6ff7c4" stop-opacity="0"/>
        </radialGradient>
        <radialGradient id="mint-glow-b" cx="0.62" cy="0.45" r="0.22">
          <stop offset="0" stop-color="#6ff7c4" stop-opacity="0.35"/>
          <stop offset="1" stop-color="#6ff7c4" stop-opacity="0"/>
        </radialGradient>
        <radialGradient id="mint-glow-c" cx="0.95" cy="0.33" r="0.12">
          <stop offset="0" stop-color="#6ff7c4" stop-opacity="0.5"/>
          <stop offset="1" stop-color="#6ff7c4" stop-opacity="0"/>
        </radialGradient>
        <radialGradient id="wave-glow" cx="0.18" cy="0.6" r="0.45">
          <stop offset="0" stop-color="#4f8fff" stop-opacity="0.55"/>
          <stop offset="1" stop-color="#4f8fff" stop-opacity="0"/>
        </radialGradient>
        <radialGradient id="top-glow" cx="0.45" cy="0.05" r="0.45">
          <stop offset="0" stop-color="#5a9cff" stop-opacity="0.55"/>
          <stop offset="1" stop-color="#5a9cff" stop-opacity="0"/>
        </radialGradient>
      </defs>
      <rect width="1116" height="1116" fill="url(#top-glow)"/>
      <rect width="1116" height="1116" fill="url(#wave-glow)"/>
      <rect width="1116" height="1116" fill="url(#mint-glow-a)"/>
      <rect width="1116" height="1116" fill="url(#mint-glow-b)"/>
      <rect width="1116" height="1116" fill="url(#mint-glow-c)"/>
      <path d="M760 1116 C860 900 1010 760 1116 700 L1116 1116 Z" fill="#1536c4" opacity="0.45"/>
      <path d="M0 1010 C320 980 580 880 780 730 C910 630 1030 500 1116 420" fill="none" stroke="#6aa8ff" stroke-opacity="0.3" stroke-width="3"/>
    </svg>

    <svg class="card-text" width="1116" height="1116" viewBox="0 0 1116 1116">
      <defs>
        <filter id="text-shadow" x="-10%" y="-20%" width="130%" height="150%">
          <feDropShadow dx="4" dy="5" stdDeviation="3" flood-color="#00083c" flood-opacity="0.85"/>
        </filter>
      </defs>

      <text class="ghost-name" x="70" y="525" textLength="720" lengthAdjust="spacing">mira</text>

      <text class="headline" x="12" y="137" textLength="1092" lengthAdjust="spacingAndGlyphs">We vinden je nu al leuk!</text>

      <text x="14" y="283"><tspan class="date-big">20</tspan><tspan class="date-small">JUNE </tspan><tspan class="date-big">2013</tspan></text>

      <text class="parents" x="1079" y="599" text-anchor="end">Dochter van Fenna</text>
      <text class="parents" x="1079" y="695" text-anchor="end">Drost &amp; Joost Kramer</text>

      <text class="contact" x="39" y="777">Yangon, Myanmar</text>
      <text class="contact" x="39" y="871">+95 1 73 4816</text>
      <text class="contact" x="39" y="971">Skype: Fenna.Drost</text>
      <text class="contact" x="39" y="1067">Skype: Joost.Kramer</text>
    </svg>
  </div>
</body>
</html>
```